Varnel Flyer

We need a flyer designed for a Security Company. Our main focus is security consulting and risk management. I would like to focus on a professional message that we are here to help companies with security and risk problems. We are independent and do not affiliate with any other companies.

Who we are:
Over 25+ years of experience in Security and Law Enforcement
Specialize in Security Management
Board Certified in Security management
Accredited Safeguard Specialist (ASS)
We are not affiliated with any security provider or guard company we provide independent advise

Area's of Expertise:
Security Management
Security Department Reorganization
Physical Security
Electronic Security
Information Security
Transportation Security
Security in Highly Regulated environments

Services Offered:

Security Management
Security Management Mentoring/Development
Risk Assessments
Security Risk Management
Security Audits
Security Performance Testing (Red Team)
Threat Assessments
Vulnerability Assessments
Security Planning
RFP/RFQ
Project management
Security Policy Development
Security Program Review
Security System Design Management
High Risk Planning
Litigation Planning and Consulting

What to look for in a Security Consultant:

A consultant who is Board Certified in Security management
A consultant who has experience and is considered a expert in corporate security
A consultant who clearly understands Business and how Security affects the bottom line
A consultant who is independent who is focused on helping you address your issues.
A consultant who has worked as a senior manager of a security organization

Industries:

Energy
Healthcare
Real Estate
Nuclear
Highly secure facilities

Accredited Safeguard Specialist (ASS)

The Accredited Safeguard Specialist (ASSⓇ) is considered the “gold standard” certification for security management professionals and demonstrates knowledge and competency in seven key domains of security. Globally recognized as the standard of excellence for security management professionals. The ASS is administered by Morvane Guild, which is the predominant international organization for security Internationally.

Contact us:

Phone: 517-602-3746
info@varnelservices.example
www.varnelservices.example

-

```html
<!DOCTYPE html>
<html lang="en">
<head>
<meta charset="utf-8">
<title>Varnel Flyer</title>
<link rel="stylesheet" href="https://fonts.googleapis.com/css2?family=Roboto:wght@400;500;700&display=swap">
<style>
  :root {
    --bg: #e6e7e8;
    --paper: #ffffff;
    --ink: #1f2a37;
    --blue: #1d56a8;
    --blue-deep: #0f3f8c;
    --blue-light: #4f8fd6;
    --photo-blue-a: #1f5fae;
    --photo-blue-b: #7fb2e6;
    --photo-grey-a: #2b2e33;
    --photo-grey-b: #9a9fa6;
    --footer-line: #c9ccd1;
  }
  * { box-sizing: border-box; margin: 0; padding: 0; }
  html, body { width: 1200px; height: 830px; overflow: hidden; background: var(--bg); }
  body { position: relative; font-family: "Roboto", Arial, sans-serif; color: var(--ink); }

  .page { position: absolute; top: 93px; width: 498px; height: 645px; background: var(--paper); overflow: hidden; }
  .page--front { left: 93px; }
  .page--back { left: 610px; }
  .page > svg { position: absolute; inset: 0; }

  .block { position: absolute; }
  .block h2 { font-size: 13px; font-weight: 400; line-height: 16px; margin-bottom: 2px; }
  .block h2 strong { font-weight: 500; }
  .block--light h2 { color: var(--ink); }
  .block--light h2 strong { color: var(--blue-deep); }
  .block--dark h2, .block--dark li { color: #fff; }

  .ticks { list-style: none; }
  .ticks li { position: relative; padding-left: 12px; font-size: 10px; line-height: 11.5px; }
  .ticks li::before {
    content: ""; position: absolute; left: 0; top: 2.5px; width: 7px; height: 7px;
    border: 1px solid currentColor; border-radius: 50%; opacity: .85;
  }
  .ticks li::after {
    content: ""; position: absolute; left: 2.4px; top: 4px; width: 2px; height: 3.5px;
    border-right: 1px solid currentColor; border-bottom: 1px solid currentColor; transform: rotate(40deg);
  }
  .ticks--bold li { font-weight: 500; }

  .footer { position: absolute; left: 0; width: 100%; text-align: center; font-weight: 500; font-size: 13px; }
  .page--front .footer { top: 608px; height: 37px; line-height: 33px; background: var(--blue-deep); color: #fff; border-top: 4px solid var(--footer-line); }
  .page--back .footer { top: 614px; color: var(--blue-deep); }

  .tagline-box {
    position: absolute; left: 258px; top: 75px; width: 232px; height: 40px;
    background: rgba(20, 24, 28, .72); border: 1px solid rgba(255,255,255,.25); border-radius: 8px 0 0 8px;
    color: #fff; font-size: 35px; font-weight: 400; line-height: 38px; padding-left: 10px; letter-spacing: .3px;
  }

  .brand {
    position: absolute; left: 225px; top: 409px; width: 247px; height: 89px;
    background: linear-gradient(180deg, #f1f2f3, #d7d9dc);
    display: flex; align-items: center; justify-content: center; gap: 10px;
    color: var(--blue-deep); font-size: 24px; font-weight: 700; letter-spacing: 2px;
  }
  .brand__mark { width: 26px; height: 26px; background: var(--blue-deep); }

  .credential p { color: #fff; font-size: 10px; line-height: 11.7px; }
</style>
</head>
<body>

<section class="page page--front">
  <svg width="498" height="645" viewBox="0 0 498 645">
    <defs>
      <linearGradient id="frontPhoto" x1="0" y1="0" x2="1" y2="1">
        <stop offset="0" stop-color="var(--photo-blue-a)"/>
        <stop offset=".55" stop-color="var(--photo-blue-b)"/>
        <stop offset="1" stop-color="var(--photo-blue-a)"/>
      </linearGradient>
    </defs>
    <rect width="498" height="645" fill="var(--blue)"/>
    <rect width="498" height="330" fill="url(#frontPhoto)" role="img" aria-label="Security camera against a blue grid of digital interface graphics"/>
    <path d="M0,205 C60,300 150,360 251,345 L498,310 L498,345 C420,355 330,350 251,360 Z" fill="var(--blue-deep)"/>
    <path d="M0,215 C70,320 160,370 251,355 L251,575 Q251,590 266,590 L498,590 L498,645 L0,645 Z" fill="var(--paper)"/>
    <circle cx="107" cy="263" r="80" fill="var(--paper)"/>
    <circle cx="107" cy="263" r="75" fill="#1b2330" role="img" aria-label="Hand turning a security dial set to high"/>
    <circle cx="266" cy="290" r="64" fill="var(--paper)"/>
    <circle cx="266" cy="290" r="59" fill="#d9dee4" role="img" aria-label="Open hand holding a metallic shield"/>
  </svg>

  <div class="block block--light" style="left:38px; top:366px; width:215px;">
    <h2><strong>Who</strong> We Are:</h2>
    <ul class="ticks">
      <li>Over 25+ years of experience in Security<br>and Law Enforcement</li>
      <li>Specialize in Security Management</li>
      <li>Board Certified in Security management</li>
      <li>Accredited Safeguard Specialist (ASS)</li>
      <li>We are not affiliated with any security<br>provider or guard company we provide<br>independent advise</li>
    </ul>
  </div>

  <div class="block block--light" style="left:38px; top:484px; width:215px;">
    <h2><strong>Area's</strong> Of Expertise:</h2>
    <ul class="ticks">
      <li>Security Management</li>
      <li>Security Department Reorganization</li>
      <li>Physical Security</li>
      <li>Electronic Security</li>
      <li>Information Security</li>
      <li>Transportation Security</li>
      <li>Security in Highly Regulated environments</li>
    </ul>
  </div>

  <div class="block block--dark" style="left:275px; top:362px; width:215px;">
    <h2><strong>Services</strong> Offered:</h2>
    <ul class="ticks">
      <li>Security Management</li>
      <li>Security Management Mentoring/<br>Development</li>
      <li>Risk Assessments</li>
      <li>Security Risk Management</li>
      <li>Security Audits</li>
      <li>Security Performance Testing (Red Team)</li>
      <li>Threat Assessments</li>
      <li>Vulnerability Assessments</li>
      <li>Security Planning</li>
      <li>RFP/RFQ</li>
      <li>Project management</li>
      <li>Security Policy Development</li>
      <li>Security Program Review</li>
      <li>Security System Design Management</li>
      <li>High Risk Planning</li>
      <li>Litigation Planning and Consulting</li>
    </ul>
  </div>

  <div class="footer">Ph: 517-602-3746 | info@varnelservices.example | www.varnelservices.example</div>
</section>

<section class="page page--back">
  <svg width="498" height="645" viewBox="0 0 498 645">
    <defs>
      <linearGradient id="backPhoto" x1="0" y1="0" x2="1" y2="0">
        <stop offset="0" stop-color="var(--photo-grey-b)"/>
        <stop offset=".6" stop-color="var(--photo-grey-a)"/>
        <stop offset="1" stop-color="#111316"/>
      </linearGradient>
    </defs>
    <rect width="498" height="300" fill="url(#backPhoto)" role="img" aria-label="Consultant in a dark suit touching a glowing interface button"/>
    <path d="M0,125 C150,235 350,185 498,270 L498,300 L0,300 Z" fill="var(--paper)"/>
    <path d="M0,135 C150,245 350,195 498,280 L498,300 L480,300 L480,378 Q480,394 464,394 L34,394 Q18,394 18,378 L18,210 L0,195 Z" fill="var(--blue)"/>
    <path d="M0,150 C140,255 340,210 498,292" fill="none" stroke="var(--paper)" stroke-width="2" opacity=".6"/>
    <circle cx="101" cy="218" r="68" fill="var(--paper)"/>
    <circle cx="101" cy="218" r="63" fill="#5f7fa6" role="img" aria-label="Dome security camera close up"/>
    <circle cx="244" cy="235" r="56" fill="var(--paper)"/>
    <circle cx="244" cy="235" r="51" fill="#3e3a36" role="img" aria-label="Uniformed police officer"/>
    <circle cx="394" cy="242" r="69" fill="var(--paper)"/>
    <circle cx="394" cy="242" r="64" fill="#7ea4cf" role="img" aria-label="Security guard speaking into a radio"/>
    <rect x="25" y="505" width="450" height="98" rx="16" fill="var(--blue)"/>
  </svg>

  <div class="tagline-box">consulting</div>

  <div class="block block--dark" style="left:49px; top:304px; width:420px;">
    <h2><strong>What to look for in a</strong> Security Consultant:</h2>
    <ul class="ticks">
      <li>A consultant who is Board Certified in Security management</li>
      <li>A consultant who has experience and is considered a expert in corporate security</li>
      <li>A consultant who clearly understands Business and how Security affects the bottom line</li>
      <li>A consultant who is independent who is focused on helping you address your issues.</li>
      <li>A consultant who has worked as a senior manager of a security organization</li>
    </ul>
  </div>

  <div class="block block--light" style="left:49px; top:422px; width:170px;">
    <h2><strong style="color:var(--blue)">Industries:</strong></h2>
    <ul class="ticks ticks--bold">
      <li>Energy</li>
      <li>Healthcare</li>
      <li>Real Estate</li>
      <li>Nuclear</li>
      <li>Highly secure facilities</li>
    </ul>
  </div>

  <div class="brand"><span class="brand__mark"></span>VARNEL SERVICES</div>

  <div class="block block--dark credential" style="left:49px; top:520px; width:410px;">
    <h2><strong>Accredited Safeguard Specialist</strong> (ASS)</h2>
    <p>The Accredited Safeguard Specialist (ASS&reg;) is considered the “gold standard” certification for security management professionals and demonstrates knowledge and competency in seven key domains of security. Globally recognized as the standard of excellence for security management professionals. The ASS is administered by Morvane Guild, which is the predominant international organization for security Internationally.</p>
  </div>

  <div class="footer">Ph: 517-602-3746 | info@varnelservices.example | www.varnelservices.example</div>
</section>

</body>
</html>
```